Bodywork Quietude Business Card Design

I want to create a very elegant and sophisticated two sided business card for my massage practice (www.bodyworkquietude.net). I have attached the logo and a PDF with some ideas down for the back of the card but I am open to suggestions. I will want to tie in a post card and flyer to the card later.
Similar colors to website would be great.
Target Market(s)
High end clientele, people looking for a sophisticated spa experience.
Industry/Entity Type
Massage
Contact Information for Business Card
Bodywork Quietude
7318 Larkspur Ave S, Suite 305
Alder Bay, WA 98412
(206) 555-0147
www.bodyworkquietude.net
Look and feel

```html
<!DOCTYPE html>
<html lang="en">
<head>
<meta charset="utf-8">
<title>Bodywork Quietude – Business Card</title>
<link rel="stylesheet" href="https://fonts.googleapis.com/css2?family=Cinzel:wght@400;500&family=Open+Sans:wght@400&display=swap">
<style>
  :root {
    --page-bg: #e9e7e4;
    --card-white: #f8f7f6;
    --navy: #1c4159;
    --navy-deep: #163549;
    --ink-light: #ffffff;
    --brand-ink: #1f3a4d;
  }
  * { box-sizing: border-box; margin: 0; padding: 0; }
  html, body {
    width: 1200px;
    height: 900px;
    overflow: hidden;
    background: var(--page-bg);
  }
  .canvas {
    width: 1200px;
    height: 900px;
    display: flex;
    align-items: center;
    justify-content: center;
  }
  .business-card {
    width: 900px;
    height: 558px;
    display: flex;
    box-shadow: 0 18px 40px rgba(0, 0, 0, 0.18);
  }
  .brand-side {
    width: 424px;
    height: 100%;
    background: var(--card-white);
    display: flex;
    align-items: center;
    justify-content: center;
    gap: 14px;
  }
  .brand-mark {
    width: 22px;
    height: 22px;
    border-radius: 50%;
    background: var(--brand-ink);
  }
  .brand-name {
    font-family: "Cinzel", serif;
    font-weight: 500;
    font-size: 27px;
    letter-spacing: 0.5px;
    color: var(--brand-ink);
  }
  .contact-side {
    position: relative;
    flex: 1;
    height: 100%;
    background: var(--navy);
    color: var(--ink-light);
    text-align: right;
    padding: 64px 30px 0 0;
  }
  .leaf-strip {
    position: absolute;
    left: 0;
    top: 0;
    width: 190px;
    height: 100%;
    background: linear-gradient(90deg, var(--navy-deep) 0%, rgba(22, 53, 73, 0.45) 55%, rgba(28, 65, 89, 0) 100%);
  }
  .contact-content { position: relative; }
  .person-name {
    font-family: "Cinzel", serif;
    font-size: 30px;
    line-height: 36px;
    letter-spacing: 0.5px;
  }
  .person-title {
    font-family: "Open Sans", sans-serif;
    font-size: 21px;
    line-height: 28px;
  }
  .company-name {
    font-family: "Cinzel", serif;
    font-size: 27px;
    line-height: 34px;
    margin-top: 172px;
  }
  .address-line {
    font-family: "Open Sans", sans-serif;
    font-size: 21px;
    line-height: 33px;
  }
  .contact-line {
    font-family: "Open Sans", sans-serif;
    font-size: 21px;
    line-height: 34px;
    display: flex;
    justify-content: flex-end;
    align-items: center;
    gap: 8px;
  }
  .contact-line.first { margin-top: 30px; }
  .contact-icon { width: 20px; height: 20px; fill: var(--ink-light); }
</style>
</head>
<body>
<main class="canvas">
  <article class="business-card">
    <section class="brand-side">
      <span class="brand-mark"></span>
      <span class="brand-name">BODYWORK QUIETUDE</span>
    </section>
    <section class="contact-side">
      <div class="leaf-strip" role="img" aria-label="Faint leaf ornament along the panel edge"></div>
      <div class="contact-content">
        <p class="person-name">DANIEL HARROW</p>
        <p class="person-title">Managing Director</p>
        <p class="company-name">BODYWORK QUIETUDE</p>
        <p class="address-line">7318 Larkspur Ave S, Suite 305</p>
        <p class="address-line">Alder Bay, WA 98412</p>
        <p class="contact-line first">(206) 555-0147
          <svg class="contact-icon" viewBox="0 0 24 24" aria-hidden="true"><path d="M6.6 10.8a15.1 15.1 0 0 0 6.6 6.6l2.2-2.2c.3-.3.7-.4 1-.2 1.1.4 2.3.6 3.6.6.6 0 1 .4 1 1V20c0 .6-.4 1-1 1A17 17 0 0 1 3 4c0-.6.4-1 1-1h3.5c.6 0 1 .4 1 1 0 1.3.2 2.5.6 3.6.1.3 0 .7-.2 1z"/></svg>
        </p>
        <p class="contact-line">www.bodyworkquietude.net
          <svg class="contact-icon" viewBox="0 0 24 24" aria-hidden="true"><circle cx="12" cy="12" r="10"/><path d="M12 2a15 15 0 0 1 0 20M12 2a15 15 0 0 0 0 20M2 12h20" stroke="#1c4159" stroke-width="1.6" fill="none"/></svg>
        </p>
      </div>
    </section>
  </article>
</main>
</body>
</html>
```